Business Card Re-Design for a Lighting Designer

I would like my business card re-designed. It is currently high gloss and they scratch too easily. I don not think the current design lends itself well to a matte finish. I have included the current design for reference along with our company logo.
Check out our website for current branding.
http://www.brambleorchidstudio.example

Updates
Some of the top contenders are muslim and it is a holiday for them. I do not want to discriminate and would expect the same courtesy for holidays we celebrate.
Target Market(s)
Interior Designers, Architects
Contact Information for Business Card
Logo - Name, Title, Address, Telephone Number and Extension, Email
Font styles to use
Requirements
Must have
- All the information listed on the current business card. If you use Red, it needs to be the red from our logo.
Nice to have
- Vertical and Horizontal Designs will be entertained.
Should not have
- Requirements for a glossy finish...should not look too corporate since we are a design firm.

```html
<!DOCTYPE html>
<html lang="en">
<head>
<meta charset="UTF-8">
<title>Bramble Orchid Studio – Business Card</title>
<link href="https://fonts.googleapis.com/css2?family=Open+Sans:wght@300;400;700&display=swap" rel="stylesheet">
<style>
  :root {
    --brand-red: #a8191f;
    --ink: #1e1e1e;
    --muted: #6b6b6b;
    --paper: #fbfbfa;
    --backdrop: #e6e3de;
  }
  * { box-sizing: border-box; margin: 0; padding: 0; }
  html, body { width: 1200px; height: 942px; overflow: hidden; }
  body {
    background: var(--backdrop);
    font-family: "Open Sans", Arial, sans-serif;
    color: var(--ink);
    display: flex;
    align-items: center;
    justify-content: center;
    gap: 60px;
  }
  .card {
    position: relative;
    width: 520px;
    height: 298px;
    background: var(--paper);
    border: 3px solid var(--brand-red);
    box-shadow: 0 10px 24px rgba(0,0,0,.18);
  }
  /* front */
  .person { position: absolute; left: 34px; top: 30px; }
  .person-name { font-weight: 300; font-size: 30px; letter-spacing: .5px; line-height: 1.1; }
  .person-title { margin-top: 4px; color: var(--brand-red); font-weight: 700; font-size: 13px; letter-spacing: 2px; }
  .divider { position: absolute; left: 24px; right: 40px; top: 112px; height: 1px; background: var(--brand-red); }
  .contacts { position: absolute; left: 34px; bottom: 30px; list-style: none; font-size: 13px; }
  .contacts li { display: flex; align-items: center; gap: 10px; line-height: 24px; }
  .contacts svg { width: 12px; height: 12px; flex: none; }
  .address { position: absolute; right: 34px; bottom: 30px; text-align: right; font-size: 13px; line-height: 24px; }
  .wordmark-small { position: absolute; right: 34px; top: 34px; display: flex; align-items: center; gap: 8px; }
  .wordmark-small .mark-square { width: 26px; height: 26px; background: var(--brand-red); }
  .wordmark-small .mark-name { font-size: 14px; font-weight: 400; color: var(--ink); letter-spacing: 1px; text-transform: uppercase; line-height: 1.2; }
  /* back */
  .card-back { display: flex; align-items: center; justify-content: center; }
  .wordmark-large { display: flex; align-items: center; gap: 16px; }
  .wordmark-large .mark-square { width: 64px; height: 64px; background: var(--brand-red); }
  .wordmark-large .mark-name { font-size: 28px; font-weight: 400; color: var(--ink); letter-spacing: 1.5px; text-transform: uppercase; line-height: 1.15; }
</style>
</head>
<body>
  <section class="card card-front" aria-label="Card front">
    <div class="person">
      <h1 class="person-name">MAREN CASTELL</h1>
      <p class="person-title">PRINCIPAL</p>
    </div>
    <div class="wordmark-small">
      <span class="mark-square"></span>
      <span class="mark-name">Bramble<br>Orchid Studio</span>
    </div>
    <div class="divider"></div>
    <ul class="contacts">
      <li>
        <svg viewBox="0 0 12 12"><rect x="3" y="0.5" width="6" height="11" rx="1" fill="none" stroke="var(--brand-red)" stroke-width="1.2"/><rect x="5" y="9" width="2" height="1" fill="var(--brand-red)"/></svg>
        555.014.2290 x1
      </li>
      <li>
        <svg viewBox="0 0 12 12"><rect x="0.5" y="2.5" width="11" height="7" fill="var(--brand-red)"/><path d="M0.5 2.5 L6 7 L11.5 2.5" fill="none" stroke="#fff" stroke-width="1"/></svg>
        maren@brambleorchidstudio.example
      </li>
      <li>
        <svg viewBox="0 0 12 12"><circle cx="6" cy="6" r="5.2" fill="none" stroke="var(--brand-red)" stroke-width="1.1"/><ellipse cx="6" cy="6" rx="2.2" ry="5.2" fill="none" stroke="var(--brand-red)" stroke-width="1"/><line x1="0.8" y1="6" x2="11.2" y2="6" stroke="var(--brand-red)" stroke-width="1"/></svg>
        www.brambleorchidstudio.example
      </li>
    </ul>
    <address class="address" style="font-style:normal">
      210 Larkspur Row, Suite 40<br>
      Fairhaven, Oregon 97000 USA
    </address>
  </section>

  <section class="card card-back" aria-label="Card back">
    <div class="wordmark-large">
      <span class="mark-square"></span>
      <span class="mark-name">Bramble<br>Orchid Studio</span>
    </div>
  </section>
</body>
</html>
```